Tech business card design

We need an amazing business card design for our new business 'Brakka' a marketing tech startup based in Sydney, Australia. We provide an online marketplace for businesses to search and buy advertising media, connect with service providers and learn more about marketing. We wish to communicate 'cool tech', reliability and professionalism and design based around our logo.

Target Market(s)

Business Owners

Contact Information for Business Card

Name
Position
Email Address
Website
Phone Number

Font styles to use
Other font styles liked:
• Avenir & Avenir Next

Colors

Designer to choose colors to be used in the design.

```html
<!DOCTYPE html>
<html lang="en">
<head>
<meta charset="utf-8">
<title>Brakka Business Card</title>
<link rel="stylesheet" href="https://fonts.googleapis.com/css2?family=Nunito+Sans:wght@400;700;800&display=swap">
<style>
  :root {
    --backdrop: #e2e2e2;
    --navy: #170f3a;
    --paper: #f4f4f4;
    --white: #ffffff;
  }
  * { margin: 0; padding: 0; box-sizing: border-box; }
  html, body {
    width: 1200px;
    height: 960px;
    overflow: hidden;
    background: var(--backdrop);
    font-family: "Nunito Sans", sans-serif;
  }
  .canvas { position: relative; width: 1200px; height: 960px; }
  .card {
    position: absolute;
    left: 335px;
    width: 534px;
    height: 327px;
  }
  .card-front {
    top: 139px;
    background: var(--navy);
    display: flex;
    align-items: center;
    justify-content: center;
  }
  .brand-name {
    color: var(--white);
    font-weight: 800;
    font-size: 84px;
    letter-spacing: -1px;
    line-height: 1;
    margin-top: -8px;
  }
  .card-back {
    top: 510px;
    background: var(--paper);
    color: var(--navy);
  }
  .identity {
    position: absolute;
    right: 287px;
    top: 143px;
    text-align: right;
  }
  .person-name {
    font-weight: 800;
    font-size: 19px;
    letter-spacing: 0.3px;
    line-height: 1.1;
  }
  .person-role {
    font-weight: 400;
    font-size: 14.5px;
    letter-spacing: 0.2px;
    margin-top: 2px;
  }
  .divider {
    position: absolute;
    left: 267px;
    top: 136px;
    width: 1px;
    height: 53px;
    background: var(--navy);
  }
  .contacts {
    position: absolute;
    left: 286px;
    top: 135px;
    list-style: none;
    font-size: 14.5px;
    line-height: 18px;
  }
  .contacts li { display: flex; align-items: center; gap: 5px; }
  .contacts svg { width: 11px; height: 11px; flex: none; }
</style>
</head>
<body>
<main class="canvas">
  <section class="card card-front">
    <span class="brand-name">Brakka</span>
  </section>

  <section class="card card-back">
    <div class="identity">
      <p class="person-name">DANIEL REEVE</p>
      <p class="person-role">FOUNDER, DIRECTOR</p>
    </div>
    <div class="divider"></div>
    <ul class="contacts">
      <li>
        <svg viewBox="0 0 12 12" aria-hidden="true"><rect x="3" y="0.7" width="6" height="10.6" rx="1" fill="none" stroke="#170f3a" stroke-width="1.1"/><line x1="5" y1="9.6" x2="7" y2="9.6" stroke="#170f3a" stroke-width="1"/></svg>
        +61 (0)400 555 218
      </li>
      <li>
        <svg viewBox="0 0 12 12" aria-hidden="true"><rect x="0.6" y="2.2" width="10.8" height="7.6" fill="none" stroke="#170f3a" stroke-width="1.1"/><path d="M0.8 2.5 L6 6.8 L11.2 2.5 M0.8 9.5 L4.5 5.7 M11.2 9.5 L7.5 5.7" fill="none" stroke="#170f3a" stroke-width="1"/></svg>
        daniel@brakkamedia.com.au
      </li>
      <li>
        <svg viewBox="0 0 12 12" aria-hidden="true"><circle cx="6" cy="6" r="5.3" fill="none" stroke="#170f3a" stroke-width="1.1"/><ellipse cx="6" cy="6" rx="2.3" ry="5.3" fill="none" stroke="#170f3a" stroke-width="0.9"/><path d="M0.7 6 H11.3 M1.6 3.3 H10.4 M1.6 8.7 H10.4" stroke="#170f3a" stroke-width="0.9"/></svg>
        www.brakkamedia.com.au
      </li>
    </ul>
  </section>
</main>
</body>
</html>
```